Personal Business Card Design Project

I am looking for a business card to be able to hand to both Chinese and Australian businessman.
I am a self employed consultant and just need my name, phone number and email address on the card. No Business Name and No Website.
I want it to look like an exclusive prestigious card.
I would like the background to be be a glossy red and the writing to be gold. (This applies to both sides of the card).
It must have English on one side and Chinese (Mandarin) on the reverse.
Details you will require
Name : Wade Emmerson
Phone : + 61 493 207 158
Email : wadeyemmerson@brightpost.example
Thank you everybody for your designs.
Industry/Entity Type
Business

```html
<!DOCTYPE html>
<html lang="en">
<head>
<meta charset="utf-8">
<title>Wade Emmerson — Business Card, English and Chinese sides</title>
<link rel="stylesheet" href="https://fonts.googleapis.com/css2?family=Noto+Sans+SC:wght@500;700&family=Source+Sans+3:wght@400;600;700&display=swap">
<style>
  :root {
    --backdrop: #ece8e2;
    --card-red-light: #a8161d;
    --card-red: #940508;
    --card-red-deep: #760000;
    --gold: #c9a653;
    --icon-ink: #141010;
  }
  * { margin: 0; padding: 0; box-sizing: border-box; }
  html, body {
    width: 1200px;
    height: 1200px;
    overflow: hidden;
    background: var(--backdrop);
  }
  .canvas {
    position: relative;
    width: 1200px;
    height: 1200px;
    font-family: "Source Sans 3", "Myriad Pro", Arial, sans-serif;
  }
  .card {
    position: absolute;
    left: 220px;
    width: 760px;
    height: 434px;
    background:
      radial-gradient(ellipse 90% 80% at 78% 18%, var(--card-red-light) 0%, var(--card-red) 45%, var(--card-red-deep) 100%);
    box-shadow: 0 10px 28px rgba(0, 0, 0, 0.18);
    color: var(--gold);
  }
  .card--english { top: 110px; }
  .card--chinese { top: 656px; }

  .card--english .card__details {
    position: absolute;
    top: 118px;
    left: 0;
    right: 0;
    text-align: center;
  }
  .card__name {
    font-weight: 700;
    font-size: 56px;
    line-height: 1;
    letter-spacing: -0.3px;
  }
  .card__line {
    font-weight: 600;
    font-size: 34px;
    line-height: 1;
    white-space: nowrap;
  }
  .card--english .card__name { margin-bottom: 34px; }
  .card--english .card__line + .card__line { margin-top: 30px; }

  .card--chinese .card__name {
    position: absolute;
    top: 62px;
    left: 130px;
    font-family: "Noto Sans SC", "Source Sans 3", sans-serif;
    font-size: 54px;
    letter-spacing: 2px;
  }
  .contact-row {
    position: absolute;
    left: 56px;
    display: flex;
    align-items: center;
    gap: 22px;
  }
  .contact-row--phone { top: 160px; left: 72px; gap: 24px; }
  .contact-row--email { top: 238px; }
  .contact-row__icon { flex: none; fill: var(--icon-ink); }
</style>
</head>
<body>
<main class="canvas">

  <section class="card card--english" lang="en" aria-label="Business card, English side">
    <div class="card__details">
      <p class="card__name">Wade Emmerson</p>
      <p class="card__line">+ 61 493 207 158</p>
      <p class="card__line">wadeyemmerson@brightpost.example</p>
    </div>
  </section>

  <section class="card card--chinese" lang="zh-Hans" aria-label="Business card, Chinese side">
    <p class="card__name">韦德·埃默森</p>
    <div class="contact-row contact-row--phone">
      <svg class="contact-row__icon" width="32" height="52" viewBox="0 0 24 52" aria-hidden="true">
        <path d="M14 2 C10 2 4 6 3 14 C1 24 2 36 8 46 C11 50 16 50 18 48 L22 42 C23 40 22 38 20 37 L15 34 C13 33 12 32 12 30 C11 27 11 23 12 21 C12 19 13 18 15 17 L20 14 C22 13 23 11 22 9 L19 4 C18 2 16 2 14 2 Z"/>
      </svg>
      <p class="card__line">+ 61 493 207 158</p>
    </div>
    <div class="contact-row contact-row--email">
      <svg class="contact-row__icon" width="52" height="38" viewBox="0 0 52 38" aria-hidden="true">
        <path d="M2 2 H50 V36 H2 Z M5 5 V33 H47 V5 Z" fill-rule="evenodd"/>
        <path d="M4 4 L26 22 L48 4" fill="none" stroke="#141010" stroke-width="2.6"/>
        <path d="M4 34 L20 18 M48 34 L32 18" fill="none" stroke="#141010" stroke-width="2.2"/>
      </svg>
      <p class="card__line">wadeyemmerson@brightpost.example</p>
    </div>
  </section>

</main>
</body>
</html>
```